agricultural technology company needs business cards*

design a business card that represents our business well. please see our website: vastrelbyfieldseal.com.au
professional, simple, clean lines, not complicated or floral.....

```html
<!DOCTYPE html>
<html lang="en">
<head>
<meta charset="utf-8">
<title>Vastrelby FieldSeal – Business Card</title>
<link rel="stylesheet" href="https://fonts.googleapis.com/css2?family=Source+Sans+3:wght@400;600;700&display=swap">
<style>
  :root {
    --navy: #1b2a55;
    --green: #2aa94a;
    --lime: #9cc43c;
    --card-white: #f4f4f4;
    --backdrop: #e4e5e6;
    --white: #ffffff;
  }
  html, body {
    margin: 0;
    padding: 0;
    width: 1200px;
    height: 960px;
    overflow: hidden;
    background: var(--backdrop);
    font-family: "Source Sans 3", "Helvetica Neue", Arial, sans-serif;
  }
  .stage { position: relative; width: 1200px; height: 960px; }
  .card {
    position: absolute;
    top: 198px;
    width: 346px;
    height: 565px;
    box-sizing: border-box;
  }
  .card--front { left: 235px; background: var(--navy); }
  .card--back { left: 620px; background: var(--card-white); }

  /* Front */
  .brand-front {
    position: absolute;
    left: 0; right: 0;
    top: 242px;
    text-align: center;
    color: var(--white);
    font-weight: 700;
    font-size: 38px;
    line-height: 40px;
    letter-spacing: -0.5px;
  }
  .tagline {
    position: absolute;
    left: 0; right: 0;
    top: 496px;
    text-align: center;
    color: var(--white);
    font-weight: 600;
    font-size: 18px;
  }
  .tagline .accent { color: var(--green); }

  /* Back */
  .brand-back {
    position: absolute;
    left: 40px;
    top: 58px;
    display: flex;
    align-items: center;
    gap: 14px;
    color: var(--navy);
    font-weight: 700;
    font-size: 36px;
    line-height: 38px;
    letter-spacing: -0.5px;
  }
  .brand-back .mark {
    width: 18px; height: 18px;
    background: var(--green);
    flex: none;
  }
  .person { position: absolute; left: 38px; top: 346px; }
  .person__name {
    margin: 0;
    color: var(--green);
    font-weight: 700;
    font-size: 19px;
    line-height: 22px;
  }
  .person__role {
    margin: 0;
    color: var(--navy);
    font-size: 14.5px;
    line-height: 18px;
  }
  .divider {
    position: absolute;
    top: 406px;
    height: 2px;
    background: var(--lime);
  }
  .divider--short { left: 0; width: 32px; background: var(--green); }
  .divider--long { left: 38px; width: 271px; }
  .contact {
    position: absolute;
    left: 38px;
    top: 424px;
    color: var(--navy);
    font-size: 14.5px;
    line-height: 19px;
  }
  .contact__address { margin: 0 0 6px; }
  .contact__line { display: flex; align-items: center; gap: 5px; margin: 0; }
  .contact__line svg { width: 12px; height: 12px; flex: none; }
  .contact .domain { color: var(--green); }
</style>
</head>
<body>
<main class="stage">
  <section class="card card--front">
    <div class="brand-front">Vastrelby<br>FieldSeal</div>
    <p class="tagline"><span class="accent">Create</span> Your Advantage.</p>
  </section>

  <section class="card card--back">
    <div class="brand-back">
      <span>Vastrelby<br>FieldSeal</span>
      <span class="mark"></span>
    </div>

    <div class="person">
      <p class="person__name">Maren Okafor</p>
      <p class="person__role">Founder &amp; Co-owner</p>
    </div>

    <div class="divider divider--short"></div>
    <div class="divider divider--long"></div>

    <div class="contact">
      <p class="contact__address">52 Tarrant Street,<br>Kelmore, WA 6172</p>
      <p class="contact__line">
        <svg viewBox="0 0 12 12" aria-hidden="true"><path fill="#2aa94a" d="M2.4 0.6l1.8 2.2-1 1.2c0.8 1.6 2 2.8 3.8 3.8l1.2-1 2.2 1.8-0.9 2.2C4.8 10.6 1.4 7.2 0.2 1.5z"/></svg>
        1300 482 316
      </p>
      <p class="contact__line">
        <svg viewBox="0 0 12 12" aria-hidden="true"><rect x="0.7" y="2.2" width="10.6" height="7.6" fill="none" stroke="#2aa94a" stroke-width="1.2"/><path d="M0.9 2.5L6 6.6l5.1-4.1" fill="none" stroke="#2aa94a" stroke-width="1.2"/></svg>
        info@vastrelbyfieldseal.com.au
      </p>
      <p class="contact__line">
        <svg viewBox="0 0 12 12" aria-hidden="true"><g fill="none" stroke="#2aa94a" stroke-width="1"><circle cx="6" cy="6" r="5.2"/><ellipse cx="6" cy="6" rx="2.2" ry="5.2"/><path d="M0.8 6h10.4M1.6 3.3h8.8M1.6 8.7h8.8"/></g></svg>
        <span>www.<span class="domain">vastrelbyfieldseal</span>.com.au</span>
      </p>
    </div>
  </section>
</main>
</body>
</html>
```